Tavosk Engineering Report Template

A word doc report Template for an Engineering Company - Tavosk

Target Market(s)

Construction/Development Industry

Industry/Entity Type

Engineering Consultant

Font styles to use
Sans Serif
Other font styles liked:
• Calibri

Colors
0455a3

Requirements
Must have
• An awesome front page, using the Tavosk Logo (not sure which version yet)
• A great back page
• Good formatting within, different heading styles which look awesome
• Format generally as the the PLW example report, no need to vary
Nice to have
• smart features? easily manipulated? not sure how tricky or smart Word is in this area.
Should not have
• LOCKED features (if possible)

```html
<!DOCTYPE html>
<html lang="en">
<head>
<meta charset="utf-8">
<title>Tavosk Engineering Report Template</title>
<link href="https://fonts.googleapis.com/css2?family=Open+Sans:wght@400;600;700&display=swap" rel="stylesheet">
<style>
:root{
  --brand:#0455a3;
  --brand-mid:#2474d0;
  --brand-light:#3d95ea;
  --ink:#222;
  --muted:#555;
  --rule:#9cc3ea;
  --stage:#cfd7d9;
  --paper:#fff;
  --row-tint:#cfe6fb;
  --row-alt:#e8f3fd;
}
*{margin:0;padding:0;box-sizing:border-box}
html,body{width:1200px;height:1200px;overflow:hidden}
body{background:var(--stage);font-family:"Open Sans",Calibri,sans-serif;color:var(--ink);position:relative}
.page{position:absolute;width:233px;height:329px;background:var(--paper);overflow:hidden;box-shadow:0 1px 3px rgba(0,0,0,.15)}
.c1{left:66px}.c2{left:346px}.c3{left:624px}.c4{left:913px}
.r1{top:63px}.r2{top:437px}.r3{top:810px}
.page svg.bg{position:absolute;inset:0;width:100%;height:100%}
.brand{display:flex;align-items:center;gap:4px;color:var(--brand);font-weight:700;letter-spacing:1px}
.brand .dot{width:9px;height:9px;background:var(--brand)}
.cover-brand{position:absolute;top:66px;left:0;right:0;justify-content:center;font-size:15px}
.cover-sub{position:absolute;top:86px;width:100%;text-align:center;font-size:4.5px;font-weight:700;letter-spacing:1px;color:var(--ink)}
.cover-title{position:absolute;left:0;right:0;text-align:center;color:#fff;font-weight:700;font-size:10.5px;line-height:1.3}
.page-title{position:absolute;top:22px;left:26px;right:26px;text-align:center;font-size:7.5px;letter-spacing:.3px;border-bottom:.8px solid var(--rule);padding-bottom:3px}
.body{position:absolute;top:42px;left:24px;right:24px;font-size:3.3px;line-height:1.55;color:var(--muted)}
.body p{margin-bottom:3px}
.body h3{color:var(--brand-mid);font-size:6px;font-weight:600;margin:4px 0 1px}
.body .lead{color:var(--brand-mid)}
.body .sub{color:var(--brand-mid);font-size:4.5px;margin-bottom:2px}
.footer{position:absolute;left:0;bottom:0;width:233px;height:12px}
.footer span{position:absolute;left:22px;bottom:3px;font-size:3px;color:#fff}
.pnum{position:absolute;right:18px;bottom:5px;font-size:3.5px;color:var(--brand)}
.toc{list-style:none}
.toc li{display:flex;font-size:3.3px;line-height:2.4;color:var(--ink)}
.toc li .lead-dots{flex:1;border-bottom:.5px dotted #888;margin:0 4px 2px}
.callout{background:var(--brand);color:#fff;display:flex;gap:6px;align-items:center;padding:3px 5px;margin-bottom:5px;font-size:3.5px}
.callout .ring{width:16px;height:16px;border-radius:50%;border:2px solid #fff;flex:none}
.photo{background:linear-gradient(135deg,#4a6782,#2c3e52 60%,#7c8c99);}
.bullets p{padding-left:6px}
table{width:100%;border-collapse:collapse;font-size:3px;margin:3px 0 5px}
th{background:var(--brand-light);color:#fff;font-weight:600;padding:1px 3px}
td{padding:1px 3px;border-bottom:.6px solid #fff;background:var(--row-alt)}
tr.phase td{background:var(--row-tint);color:var(--brand)}
tr.total td{background:var(--brand-light);color:#fff;font-weight:600}
td.n{text-align:center}
.two-col{display:flex;gap:8px}
.two-col .pics{width:80px;flex:none}
.contact{position:absolute;bottom:30px;left:46px;display:flex;gap:8px;align-items:center;font-size:2.8px;color:var(--brand);line-height:1.6}
.contact .ico{display:inline-block;width:4px;height:4px;border-radius:50%;background:var(--brand);margin-right:2px;vertical-align:middle}
</style>
</head>
<body>

<!-- Front cover -->
<section class="page c1 r1">
  <svg class="bg" viewBox="0 0 233 329" preserveAspectRatio="none">
    <rect y="142" width="233" height="11" fill="var(--brand-light)"/>
    <rect y="153" width="233" height="176" fill="var(--brand-mid)"/>
  </svg>
  <div class="brand cover-brand"><span class="dot"></span>TAVOSK</div>
  <div class="cover-sub">CONSULTING ENGINEERS</div>
  <h1 class="cover-title" style="top:265px">LOREM IPSUM IS SIMPLY<br>DUMMY HAS BEEN</h1>
</section>

<!-- Inside cover -->
<section class="page c2 r1">
  <svg class="bg" viewBox="0 0 233 329" preserveAspectRatio="none">
    <rect width="233" height="329" fill="var(--brand-mid)"/>
    <polygon points="0,262 233,200 233,221 0,277" fill="var(--brand-light)"/>
    <polygon points="0,268 233,221 233,329 0,329" fill="#fff"/>
  </svg>
  <h1 class="cover-title" style="top:88px">LOREM IPSUM IS SIMPLY<br>DUMMY HAS BEEN</h1>
  <div class="brand" style="position:absolute;top:292px;left:140px;font-size:10px"><span class="dot" style="width:7px;height:7px"></span>TAVOSK</div>
  <div style="position:absolute;top:305px;left:140px;font-size:3.3px;font-weight:700;letter-spacing:.6px">CONSULTING ENGINEERS</div>
</section>

<!-- Table of contents -->
<section class="page c3 r1">
  <h2 class="page-title">TABLE OF CONTENTS</h2>
  <div class="body" style="top:48px">
    <h3 style="font-size:5.5px;margin-bottom:4px">Contents</h3>
    <ul class="toc">
      <li>Table of Contents<span class="lead-dots"></span>01</li>
      <li>Executive Summary<span class="lead-dots"></span>02</li>
      <li>Our Understanding of Your Needs<span class="lead-dots"></span>02</li>
      <li>Our Recommendations<span class="lead-dots"></span>03</li>
      <li>Our Approach<span class="lead-dots"></span>05</li>
      <li>Budget and Timeframe<span class="lead-dots"></span>07</li>
      <li>Appendix A: About Harlow Creek<span class="lead-dots"></span>10</li>
      <li>Appendix B: Selected Client List<span class="lead-dots"></span>10</li>
      <li>Appendix C: Our Capabilities<span class="lead-dots"></span>11</li>
      <li>Appendix D: Our Process<span class="lead-dots"></span>12</li>
    </ul>
  </div>
  <svg class="footer" viewBox="0 0 233 12"><polygon points="0,6 75,6 81,12 0,12" fill="var(--brand)"/><polygon points="75,6 79,6 85,12 81,12" fill="var(--brand-light)"/></svg>
  <div class="footer"><span>www.tavosk-eng.com</span></div><div class="pnum">1</div>
</section>

<!-- Headline page 2 -->
<section class="page c4 r1">
  <h2 class="page-title">HEADLINE HERE</h2>
  <div class="body">
    <h3>Solution</h3>
    <p class="sub" style="font-size:3.3px">AI automated accounting</p>
    <p>Ledgrow builds automation in stages on top of its current system to reach full accounting thanks to the Ledgrow AI. The tool automates every manual task performed by the user. It starts by connecting to all sources of accounting data such as bank accounts, credit cards, webshops or document management systems. Based on these data, the AI creates bookings and generates financial reports, with a chat-like interface that allows users to communicate seamlessly with it.</p>
    <p class="sub" style="font-size:3.3px">Blockchain software license or Token-as-a-License</p>
    <p>It is possible to create tokens on blockchain that represent software licenses, also known as Token-as-a-License. Ledgrow creates these by using the Velton wallet which interacts with the Velton blockchain. Upon purchase, the token holder is free to transfer or sell it using a secondary market built directly over the blockchain. Ledgrow checks the validity of a token against the blockchain ensuring that token holders have access to the software, making the management and resale of licenses easier for software owners.</p>
    <h3>Pre-ICO Token sale</h3>
    <p>To realize this innovative vision, Ledgrow is launching a pre-ICO in form of a token sale on the Velton blockchain. Tokens are available to purchase for a fixed price during a thirty-day period to be announced. Tokens represent lifelong software licenses and by purchasing enough tokens, holders gain access to the software for accounting and invoicing. Future customers will still have the opportunity to buy directly yearly or monthly subscriptions.</p>
    <h3>Future plans</h3>
    <p>A future ICO is planned between 18 and 24 months after the pre-ICO token sale. This offering will support the development of Ledgrow into a fully decentralized, privacy-focused ecosystem of applications. The new model will reward each participant so that a new world with zero administrative tasks becomes reality.</p>
  </div>
  <svg class="footer" viewBox="0 0 233 12"><polygon points="0,6 75,6 81,12 0,12" fill="var(--brand)"/><polygon points="75,6 79,6 85,12 81,12" fill="var(--brand-light)"/></svg>
  <div class="footer"><span>www.tavosk-eng.com</span></div><div class="pnum">2</div>
</section>

<!-- Vision -->
<section class="page c1 r2">
  <h2 class="page-title">VISION</h2>
  <div class="body">
    <div class="callout"><span class="ring"></span><span>Ledgrow's mission is to help and support the self-employed and small business owners with their administrative tasks so they can focus on what matters – their business.</span></div>
    <p class="lead">Administrative tasks are cumbersome, time-consuming and often prevent small owners from focusing their time and energy on their business and their customers. They can also be extremely stressful for those attempting these tasks for the first time.</p>
    <p style="text-align:center">At Ledgrow, we envisage accounting for the self-employed and small business owners as being <span class="lead">automated and decentralized</span></p>
    <p>Accounting can and should be done automatically. By connecting to all sources of accounting data such as bank accounts, payment systems, e-commerce websites and invoicing systems, the AI automatically completes these tasks, which would take hours to do manually. Bookings are created automatically and fully completed, and financial statements are available within a couple of clicks.</p>
    <p>What may seem like a pipedream to the millions of self-employed who struggle with their admin is already a reality. Now is the time to join Ledgrow on its mission to transform the world of bookkeeping through the power of AI.</p>
    <h3>The Ledgrow model</h3>
    <p>Ledgrow is based on an innovative license model that uses Token-as-a-License. The token represents lifelong software license for its solutions. The pre-ICO token sales will enable the company to complete its development of AI to deliver fully automatic bookkeeping.</p>
    <p>The pre-ICO token sale will also pave the way for a future ICO. Ledgrow will launch accounting on the blockchain and ensure your accounting data is comprehensive and private, but available everywhere within your preferred apps. Furthermore, a new range of business apps will connect to provide you with leading edge business data access.</p>
    <p>Ledgrow supports strong data ownership laws that truly protect individuals and ensure they have complete ownership of their data, deciding how it should be used.</p>
    <p>To find out more about the project and the token, or if you are interested in purchasing, please register with your email at <span class="lead" style="text-decoration:underline">www.ledgrow.io/ico</span> so we can reach you.</p>
  </div>
  <svg class="footer" viewBox="0 0 233 12"><polygon points="0,6 75,6 81,12 0,12" fill="var(--brand)"/><polygon points="75,6 79,6 85,12 81,12" fill="var(--brand-light)"/></svg>
  <div class="footer"><span>www.tavosk-eng.com</span></div><div class="pnum">3</div>
</section>

<!-- Headline with photo -->
<section class="page c2 r2">
  <h2 class="page-title">HEADLINE HERE</h2>
  <div class="body" style="top:40px">
    <div class="photo" role="img" aria-label="Photo of a stressed businessman at his desk with a colleague's hand on his shoulder" style="height:83px;margin-bottom:8px"></div>
    <p class="lead">Ledgrow's mission is to help and support the self-employed and small business owners with their administrative tasks so they can focus on what matters – their business.</p>
    <p>Administrative tasks are cumbersome, time-consuming and often prevent small owners from focusing their time and energy on their business and their customers. They can also be extremely stressful and nerve-wracking for those attempting these tasks for the first time.</p>
    <p>At Ledgrow, we envisage accounting for the self-employed and small business owners as being <span class="lead">automated and decentralized</span></p>
    <p>Accounting can and should be done automatically. By connecting to all sources of accounting data such as bank accounts, payment systems, e-commerce websites and invoicing systems, the AI automatically completes these tasks. Bookings are created automatically and fully completed, and financial statements are available within a couple of clicks.</p>
    <p>What may seem like a pipedream to the millions of self-employed who struggle with their admin is already a reality. Now is the time to join Ledgrow on its mission to transform the world of bookkeeping through the power of AI.</p>
    <h3>The Ledgrow model</h3>
    <p>Ledgrow is based on an innovative license model that uses Token-as-a-License. The token represents lifelong software license for its solutions. The pre-ICO token sales will enable the company to complete its development of AI to deliver fully automatic bookkeeping.</p>
    <p>with leading edge business data access to ensure you have the best available data at your fingertips.</p>
  </div>
  <svg class="footer" viewBox="0 0 233 12"><polygon points="0,6 75,6 81,12 0,12" fill="var(--brand)"/><polygon points="75,6 79,6 85,12 81,12" fill="var(--brand-light)"/></svg>
  <div class="footer"><span>www.tavosk-eng.com</span></div><div class="pnum">7</div>
</section>

<!-- Our understanding -->
<section class="page c3 r2">
  <h2 class="page-title">OUR UNDERSTANDING OF YOUR NEEDS</h2>
  <div class="body">
    <p style="color:var(--ink)">In the last two weeks of January we conducted high level conversations both with your staff and your technology partner Northwick. As a result of those conversations we've been able to gather the following high level goals for your project:</p>
    <p style="font-size:5px;color:var(--muted);line-height:1.3">CloudDesk must be in place to support BrightPath at launch and as the program evolves</p>
    <p class="lead">The most critical aspect of this implementation both in terms of time sensitivity as well as functionality is centered around the support for the BrightPath project. Our current understanding of this project and how it relates to CloudDesk is as follows:</p>
    <div class="bullets" style="color:var(--ink)">
      <p>■ BrightPath will be comprised of a series of websites focused on organizing institutions and individuals within six specific community sectors with the goal of increased institutional and public support, to minimize risks and maximize opportunities of a changing climate.</p>
      <p>■ The primary goals of the CRM application are:</p>
      <div class="lead" style="padding-left:14px">
        <p>▶ capture information of individuals and organizations (along with their respective roles)</p>
        <p>▶ track their progress on their site specific to-do lists and site interactions</p>
        <p>▶ allow GreenField to push out next steps (ideally in an automated style) related to their to do list progress and online interactions</p>
        <p>▶ infuse GreenField's online and offline marketing program with useful segmentation information</p>
        <p>▶ natively integrate with both the BrightPath family of sites as well as the email service provider of choice</p>
      </div>
      <p>■ The data architecture must be well defined but flexible to support the core needs of the sites as launch as well as anticipated needs in the future.</p>
      <div class="lead" style="padding-left:14px">
        <p>▶ For instance, the faith based site may collect a "denomination" field, while other sites may not collect that field.</p>
        <p>▶ Future interactions outside of the to-do list may become necessary to track and GreenField will need a systemic way to capture those interactions, be able to segment on them and potentially provide automated marketing around those similar to the to-do list.</p>
      </div>
      <p>■ The information collected from the BrightPath sites must be combined with current information held within GreenField and provide a holistic view of institutions and individuals.</p>
    </div>
  </div>
  <svg class="footer" viewBox="0 0 233 12"><polygon points="0,6 75,6 81,12 0,12" fill="var(--brand)"/><polygon points="75,6 79,6 85,12 81,12" fill="var(--brand-light)"/></svg>
  <div class="footer"><span>www.tavosk-eng.com</span></div><div class="pnum">6</div>
</section>

<!-- Budget and timeframe -->
<section class="page c4 r2">
  <h2 class="page-title">BUDGET AND TIMEFRAME</h2>
  <div class="body">
    <h3 style="margin-top:0">Implementation Estimate</h3>
    <p style="color:var(--ink)">The bulk of the implementation costs will be defined by discovery. Based on similar CRM implementation projects, we feel expect that the CRM side will be something fall between 200 and 300 hours, give or take. The wide swing in hours in phase one is related to the under-defined nature of both the integration needs and our role in the integration project. Our focus in discovery will be to nail down those requirements and our role as it relates to what is needed to integrate the sites with the CRM.</p>
    <table>
      <tr><th>Task</th><th>Hours</th><th>Cost</th></tr>
      <tr><td>Discovery</td><td class="n">40</td><td class="n">$8,000</td></tr>
      <tr class="phase"><td colspan="3">Phase 1</td></tr>
      <tr><td>Discovery</td><td class="n">20-40</td><td class="n">$8,000</td></tr>
      <tr><td>Discovery</td><td class="n">20-40</td><td class="n">$8,000</td></tr>
      <tr><td>Discovery</td><td class="n">20-40</td><td class="n">$8,000</td></tr>
      <tr><td>Total Phase 1</td><td class="n">80-240</td><td class="n">$16,800-40,000</td></tr>
      <tr class="phase"><td colspan="3">Phase 2</td></tr>
      <tr><td>Discovery</td><td class="n">20-40</td><td class="n">$8,000</td></tr>
      <tr><td>Total Phase 2</td><td class="n">80-240</td><td class="n">$16,800-40,000</td></tr>
      <tr class="total"><td>Total Estimated Implementation Cost</td><td class="n">220-480</td><td class="n">$44,000-96,000</td></tr>
    </table>
    <h3>Project Timeline</h3>
    <p style="color:var(--ink)">Based on the information we have at our disposal, the March launch date doesn't seem a realistic goal to get both the work done needed to provide the foundation for the future CRM instance and the integration given the state of apparent flux of the requirements. That said, we feel it prudent to proceed with discovery before committing to or pushing that date. We are currently estimating that the first phase will take somewhere between 7 and 12 weeks (including discovery) to complete.</p>
    <table>
      <tr><th>Task</th><th>Weeks to Complete</th></tr>
      <tr><td>Discovery</td><td class="n">1-2</td></tr>
      <tr><td>Phase 1</td><td class="n">6-10</td></tr>
      <tr><td>Phase 2</td><td class="n">8-12</td></tr>
      <tr><td>Total Number of Weeks</td><td class="n"></td></tr>
    </table>
  </div>
  <svg class="footer" viewBox="0 0 233 12"><polygon points="0,6 75,6 81,12 0,12" fill="var(--brand)"/><polygon points="75,6 79,6 85,12 81,12" fill="var(--brand-light)"/></svg>
  <div class="footer"><span>www.tavosk-eng.com</span></div><div class="pnum">5</div>
</section>

<!-- Headline with two photos -->
<section class="page c1 r3">
  <h2 class="page-title">HEADLINE HERE</h2>
  <div class="body" style="top:41px">
    <div class="two-col">
      <div class="pics">
        <div class="photo" role="img" aria-label="Photo of a worried businessman holding his head at a desk" style="height:122px;margin-bottom:24px"></div>
        <div class="photo" role="img" aria-label="Photo of a businessman reviewing paperwork at a table" style="height:108px"></div>
      </div>
      <div>
        <p class="lead">Ledgrow's mission is to help and support the self-employed and small business owners with their administrative tasks so they can focus on what matters – their business.</p>
        <p>Administrative tasks are cumbersome, time-consuming and often prevent small owners from focusing their time and energy on their business and their customers. They can also be extremely stressful and nerve-wracking for those attempting these tasks for the first time.</p>
        <p>At Ledgrow, we envisage accounting for the self-employed and small business owners as being <span class="lead">automated and decentralized</span></p>
        <p>Accounting can and should be done automatically. By connecting to all sources of accounting data such as bank accounts, payment systems, e-commerce websites and invoicing systems, the AI automatically completes these tasks, which would take hours to do manually. Bookings are created automatically and fully completed. Financial statements are available within a couple of clicks, and after analysing your data, the AI will offer you tips to improve your financial stability.</p>
        <p>What may seem like a pipedream to the millions of self-employed who struggle with</p>
        <h3>The Ledgrow model</h3>
        <p>Ledgrow is based on an innovative license model that uses Token-as-a-License. The token represents lifelong software license for its solutions. The pre-ICO token sales will enable the company to complete its development of AI to deliver fully automatic bookkeeping.</p>
      </div>
    </div>
  </div>
  <svg class="footer" viewBox="0 0 233 12"><polygon points="0,6 75,6 81,12 0,12" fill="var(--brand)"/><polygon points="75,6 79,6 85,12 81,12" fill="var(--brand-light)"/></svg>
  <div class="footer"><span>www.tavosk-eng.com</span></div><div class="pnum">8</div>
</section>

<!-- Back cover -->
<section class="page c2 r3">
  <svg class="bg" viewBox="0 0 233 329" preserveAspectRatio="none">
    <rect width="233" height="262" fill="var(--brand-mid)"/>
    <polygon points="0,254 233,182 233,202 0,262" fill="var(--brand-light)"/>
    <polygon points="0,262 233,202 233,329 0,329" fill="#fff"/>
  </svg>
  <div class="contact">
    <div>
      <div class="brand" style="font-size:6px"><span class="dot" style="width:4px;height:4px"></span>TAVOSK</div>
      <div style="font-size:2.4px;color:var(--ink);font-weight:700">CONSULTING ENGINEERS</div>
    </div>
    <div>
      <div><span class="ico"></span>000-555-0142 Ext 101</div>
      <div><span class="ico"></span>hello@tavosk-eng.com</div>
      <div><span class="ico"></span>www.tavosk-eng.com</div>
    </div>
    <div style="border-left:.5px solid var(--rule);padding-left:6px">
      <div>1204 North Ridge Street</div>
      <div>Suite 8, Lakeview OH 00000</div>
    </div>
  </div>
</section>

</body>
</html>
```